exciting cleaing project

I need a cleaning website built. It has to be built for a woman. the domain name is gwenshines.net.

I need the designer to find the images and code the site. the site needs to be about five pages.

here are some good examples:

https://www.tidypetal.com/gainesville/

http://abrightwren.com/

https://brisknookgainesville.com/services/

https://www.hevo.com/housekeepers/gainesville-fl

https://glintrow.com/

Target Market(s)

home cleaning,

Industry/Entity Type

Cleaning Service

Coding

Coded - Design and coding required

Number of Pages Required

4 page

Font styles to use
Script

Colors
33a6d7
85acd3
f04a50
ec1f27

Requirements
Must have
• nice design
Nice to have
• residential
Should not have
• commercial

```html
<!DOCTYPE html>
<html lang="en">
<head>
<meta charset="utf-8">
<title>Gwen Shines – Home Cleaning</title>
<link href="https://fonts.googleapis.com/css2?family=Montserrat:wght@400;500;600;700;800&family=Open+Sans:wght@400;600&family=Kaushan+Script&display=swap" rel="stylesheet">
<style>
:root{
  --navy:#15306b;
  --navy-deep:#0f2656;
  --blue:#2a5db0;
  --sky:#33a6d7;
  --lavender:#eef0f8;
  --yellow:#f9d71c;
  --ink:#1f2433;
  --muted:#6b7183;
  --white:#ffffff;
}
*{box-sizing:border-box;margin:0;padding:0}
html,body{width:1200px;height:3536px;overflow:hidden}
body{font-family:"Open Sans",sans-serif;color:var(--ink);background:var(--white);position:relative}
section,header,footer{position:absolute;left:0;width:1200px}
.script{font-family:"Kaushan Script",cursive;font-weight:400}
.btn{display:inline-block;background:var(--yellow);color:var(--ink);font:600 12px "Montserrat",sans-serif;padding:9px 22px;border-radius:20px}
.ph{position:absolute}

/* header */
.site-header{top:0;height:104px;background:var(--white)}
.brand{position:absolute;left:236px;top:22px;display:flex;align-items:center;gap:10px;font:700 24px "Montserrat",sans-serif;color:var(--navy)}
.brand i{width:30px;height:30px;background:var(--sky);border-radius:50%;display:block}
.top-contact{position:absolute;right:236px;top:20px;display:flex;gap:24px;font:500 12px "Montserrat",sans-serif;color:var(--navy);align-items:center}
.top-contact .phone{font-weight:700;font-size:16px;color:var(--blue)}
.top-contact span{display:flex;align-items:center;gap:8px}
.top-contact b{width:22px;height:22px;border-radius:50%;background:var(--navy);display:inline-block}
.nav{position:absolute;left:236px;right:236px;top:68px;height:28px;display:flex;align-items:center;gap:44px;font:600 12px "Montserrat",sans-serif;color:var(--navy)}
.nav .active{background:var(--navy);color:#fff;padding:6px 14px;border-radius:3px}
.nav .cta{margin-left:auto;background:var(--navy);color:#fff;padding:6px 14px;border-radius:14px}

/* hero */
.hero{top:104px;height:488px}
.hero .ph{inset:0;background:linear-gradient(100deg,#b9b4ad 0%,#e6e1d9 45%,#efe8e0 70%,#cfc6bb 100%)}
.hero-badge{position:absolute;left:266px;top:92px;width:76px;height:76px;border-radius:50%;background:var(--yellow);color:var(--navy);text-align:center;font:800 20px "Montserrat",sans-serif;padding-top:16px;line-height:1}
.hero-badge small{display:block;font:600 8px "Montserrat",sans-serif;margin-top:4px}
.hero-circle{position:absolute;left:272px;top:68px;width:296px;height:296px;border-radius:50%;background:var(--blue);border:8px solid rgba(255,255,255,.85);color:#fff;text-align:center;padding-top:92px}
.hero-circle .script{font-size:36px;color:var(--yellow);line-height:1}
.hero-circle h1{font:700 26px "Montserrat",sans-serif;line-height:1.25;margin-top:8px}
.hero-badge{z-index:2}
.dots{position:absolute;display:flex;gap:6px}
.dots i{width:8px;height:8px;border-radius:50%;background:#fff;opacity:.6;display:block}
.dots i.on{opacity:1}
.hero .dots{left:576px;top:404px}

/* about */
.about{top:592px;height:408px}
.about .logo{position:absolute;left:236px;top:88px;font:700 38px "Montserrat",sans-serif;color:var(--navy)}
.about .tag{position:absolute;left:236px;top:136px;font:600 14px "Montserrat",sans-serif;color:var(--navy)}
.about p{position:absolute;left:236px;top:172px;width:380px;font-size:12px;line-height:1.7;color:var(--muted)}
.about .note{top:262px;font-size:11px}
.about .btn{position:absolute;left:236px;top:292px}
.about .ph{left:626px;top:40px;width:340px;height:340px;border-radius:50%;background:radial-gradient(circle at 45% 40%,#e8eef6 0%,#b9cde6 60%,#5f87c2 100%)}

/* provide */
.provide{top:1000px;height:512px;background:var(--lavender);text-align:center}
.provide h2{position:absolute;left:0;right:0;top:64px;font:700 30px "Montserrat",sans-serif;color:var(--navy)}
.provide h2 .script{color:var(--blue)}
.provide .sub{position:absolute;left:0;right:0;top:108px;font-size:12px;color:var(--muted)}
.cards{position:absolute;left:236px;top:148px;width:728px;display:flex;justify-content:space-between}
.card{width:216px;text-align:center}
.card .ph{position:relative;display:block;margin:0 auto;width:124px;height:124px;border-radius:50%;background:radial-gradient(circle,#f3f4f7 0%,#d6d9e2 100%);border:6px solid #fff}
.card h3{font:700 14px "Montserrat",sans-serif;color:var(--navy);margin-top:18px}
.card .small{font-size:10px;color:var(--muted);margin-top:2px}
.card p{font-size:10.5px;line-height:1.6;color:var(--muted);margin-top:12px;height:68px}
.card .btn{margin-top:12px;padding:7px 22px;font-size:11px}

/* gallery */
.gallery{top:1512px;height:476px;background:linear-gradient(90deg,var(--navy-deep),#24509c 50%,var(--navy-deep));text-align:center;color:#fff}
.gallery .logo{position:absolute;left:0;right:0;top:56px;font:700 34px "Montserrat",sans-serif;color:var(--white)}
.gallery .sub{position:absolute;left:0;right:0;top:100px;font-size:12px;opacity:.85}
.rooms{position:absolute;left:236px;top:136px;width:728px;display:flex;justify-content:space-between}
.room{width:232px}
.room .ph{position:relative;display:block;height:174px;border:5px solid #fff}
.room:nth-child(1) .ph{background:linear-gradient(160deg,#d9c7a8,#8c6e4d)}
.room:nth-child(2) .ph{background:linear-gradient(160deg,#f2f2f0,#b9bdc2)}
.room:nth-child(3) .ph{background:linear-gradient(160deg,#ece8e1,#a59b8c)}
.room h3{font:700 14px "Montserrat",sans-serif;margin-top:12px}
.gallery .btn{position:absolute;left:556px;top:392px;font-size:11px}

/* features */
.features{top:1988px;height:204px;background:var(--yellow)}
.feature-row{position:absolute;left:236px;top:62px;width:728px;display:flex;justify-content:space-between}
.feature{width:170px;text-align:center;font:700 12px "Montserrat",sans-serif;color:var(--ink)}
.feature svg{display:block;margin:0 auto 14px}

/* reviews */
.reviews{top:2192px;height:320px;text-align:center}
.reviews h2{position:absolute;left:0;right:0;top:54px;font:700 26px "Montserrat",sans-serif;color:var(--navy)}
.reviews h2 .script{color:var(--blue)}
.reviews .ph{left:282px;top:118px;width:108px;height:108px;border-radius:50%;background:radial-gradient(circle,#dde6f1,#8fa8c9);border:5px solid #fff;box-shadow:0 0 0 2px #e1e5ee}
.reviews blockquote{position:absolute;left:418px;top:120px;width:500px;text-align:left;font-size:15px;line-height:1.7;color:var(--muted)}
.reviews cite{position:absolute;left:418px;top:212px;font:italic 11px "Open Sans",sans-serif;color:var(--muted)}
.reviews cite b{font-style:normal;color:var(--ink)}
.reviews .dots{left:572px;top:260px}
.reviews .dots i{background:var(--sky)}

/* quote */
.quote{top:2512px;height:536px}
.quote .ph{inset:0;background:linear-gradient(90deg,#e3ddd3 0%,#e9dfd2 40%,#d8b79c 70%,#c89e7e 100%)}
.quote-box{position:absolute;left:232px;top:48px;width:368px;height:420px;background:var(--navy);color:#fff;padding:40px 28px;text-align:center}
.quote-box h2{font:700 26px "Montserrat",sans-serif}
.quote-box h2 .script{color:var(--yellow)}
.quote-box .sub{font-size:12px;margin-top:6px;opacity:.9}
.fields{display:grid;grid-template-columns:1fr 1fr;gap:12px;margin-top:28px}
.field{background:#fff;height:32px;border-radius:2px;color:#9aa0ad;font-size:10px;text-align:left;padding:10px}
.field.wide{grid-column:1/3;height:70px}
.quote-box .btn{margin-top:20px;padding:8px 24px}

/* offer */
.offer{top:3048px;height:152px;background:var(--yellow)}
.offer h2{position:absolute;left:236px;top:42px;font:700 22px "Montserrat",sans-serif;color:var(--navy)}
.offer p{position:absolute;left:236px;top:74px;font:700 26px "Montserrat",sans-serif;color:var(--blue);font-style:italic}
.offer .btn{position:absolute;right:236px;top:62px;background:var(--navy);color:#fff}

/* footer */
.site-footer{top:3200px;height:336px;background:var(--navy-deep);color:#cdd6ea}
.site-footer .brand{left:236px;top:44px;color:#fff;font-size:18px}
.site-footer .brand i{width:22px;height:22px}
.contact-col{position:absolute;left:276px;top:84px;font-size:11px;line-height:1.9}
.contact-col h4,.col h4{font:700 12px "Montserrat",sans-serif;color:#fff;margin-bottom:6px}
.contact-col .phone{font:700 16px "Montserrat",sans-serif;color:var(--yellow)}
.vline{position:absolute;left:262px;top:84px;width:1px;height:170px;background:#3c5a94}
.col{position:absolute;top:84px;font-size:11px;line-height:1.9}
.social{position:absolute;left:726px;top:270px;display:flex;gap:10px}
.social i{width:22px;height:22px;border-radius:50%;border:1px solid #6b83b5;display:block}
.copy{position:absolute;left:236px;top:300px;font-size:10px;opacity:.7}
</style>
</head>
<body>

<header class="site-header">
  <div class="brand"><i></i>Gwen Shines</div>
  <div class="top-contact">
    <span><b></b>hello@gwenshines.net</span>
    <span><b></b><span class="phone">800.555.0142</span></span>
  </div>
  <nav class="nav">
    <span class="active">Home</span><span>About Company</span><span>Services</span><span>Why Gwen Shines</span><span>Reviews</span><span>Contact Us</span><span class="cta">Get Free Quote</span>
  </nav>
</header>

<section class="hero">
  <div class="ph" role="img" aria-label="Photo of a smiling cleaner wiping a bright living room"></div>
  <div class="hero-circle">
    <div class="script">Let's Make</div>
    <h1>Your House Shine and<br>Sparkle</h1>
  </div>
  <div class="hero-badge">30<small>YEARS OF<br>SERVICE</small></div>
  <div class="dots"><i class="on"></i><i></i><i></i><i></i></div>
</section>

<section class="about">
  <div class="logo">Gwen Shines</div>
  <div class="tag">Reliable &amp; Honest</div>
  <p>Our mission at Gwen Shines is to provide high quality residential cleaning you can trust. Our friendly team shows up on time, treats your home with care and leaves every room fresh, so you can enjoy more free time with the people you love.</p>
  <p class="note">Our team is fully insured and background checked.</p>
  <span class="btn">Get A Free Quote</span>
  <div class="ph" role="img" aria-label="Photo of two cheerful cleaners holding supplies in a circle frame"></div>
</section>

<section class="provide">
  <h2>What We <span class="script">Provide</span></h2>
  <div class="sub">Homes of every size, cleaned to a sparkle</div>
  <div class="cards">
    <div class="card">
      <span class="ph" role="img" aria-label="Photo of a tidy living room"></span>
      <h3>Move-in/Out Cleaning</h3><div class="small">Fresh start</div>
      <p>We clean every corner before you move in or after you move out so your keys change hands with a spotless home.</p>
      <span class="btn">More</span>
    </div>
    <div class="card">
      <span class="ph" role="img" aria-label="Photo of cleaning gloves and sponges"></span>
      <h3>Deep Cleaning</h3><div class="small">Top to bottom</div>
      <p>Baseboards, vents, cabinets and tile grout all get careful attention for a thorough, lasting shine.</p>
      <span class="btn">More</span>
    </div>
    <div class="card">
      <span class="ph" role="img" aria-label="Photo of a neat modern bedroom"></span>
      <h3>Modern Bedroom</h3><div class="small">Calm and fresh</div>
      <p>Fresh linens, dusted shelves and clear floors turn your bedroom into a peaceful space to rest.</p>
      <span class="btn">More</span>
    </div>
  </div>
</section>

<section class="gallery">
  <div class="logo">Gwen Shines</div>
  <div class="sub">Clean, comfortable and cared for rooms</div>
  <div class="rooms">
    <div class="room"><span class="ph" role="img" aria-label="Photo of a clean bedroom interior"></span><h3>Bedroom Interior</h3></div>
    <div class="room"><span class="ph" role="img" aria-label="Photo of a clean white bathroom"></span><h3>Bathrooms</h3></div>
    <div class="room"><span class="ph" role="img" aria-label="Photo of a clean dining room"></span><h3>Dining Room</h3></div>
  </div>
  <span class="btn">View All</span>
</section>

<section class="features">
  <div class="feature-row">
    <div class="feature">
      <svg width="40" height="40" viewBox="0 0 40 40"><path d="M6 18h7v18H6zM15 36V18l7-12c3 0 4 2 3 5l-2 6h10c2 0 3 2 3 3l-3 13c-1 2-2 3-4 3z" fill="var(--ink)"/></svg>
      5+ Years of Experience</div>
    <div class="feature">
      <svg width="40" height="40" viewBox="0 0 40 40"><path d="M14 4h12v5H14zM12 9h16l2 6H10zM10 15h20v21H10z" fill="var(--ink)"/></svg>
      Quality Cleaning Tools</div>
    <div class="feature">
      <svg width="40" height="40" viewBox="0 0 40 40"><circle cx="20" cy="21" r="15" fill="none" stroke="var(--ink)" stroke-width="4"/><path d="M20 12v10l7 4" stroke="var(--ink)" stroke-width="4" fill="none"/></svg>
      Fast and Effective Service</div>
    <div class="feature">
      <svg width="40" height="40" viewBox="0 0 40 40"><circle cx="20" cy="13" r="8" fill="var(--ink)"/><path d="M5 37c0-9 7-14 15-14s15 5 15 14z" fill="var(--ink)"/></svg>
      Highly Trained Staff</div>
  </div>
</section>

<section class="reviews">
  <h2>See Our Satisfied <span class="script">Customers</span> Reviews</h2>
  <div class="ph" role="img" aria-label="Customer portrait photo"></div>
  <blockquote>They are always very responsive and quick to address any concerns we might have. They are willing to go the extra mile to make every situation right.</blockquote>
  <cite><b>Mara Quill</b> – Happy home client, Gainesville</cite>
  <div class="dots"><i class="on"></i><i></i><i></i><i></i></div>
</section>

<section class="quote">
  <div class="ph" role="img" aria-label="Photo of a smiling mother and daughter at home"></div>
  <div class="quote-box">
    <h2>Get <span class="script">Free</span> Quote</h2>
    <div class="sub">Instantly and book your service Today!</div>
    <div class="fields">
      <div class="field">Full Name</div><div class="field">Email</div>
      <div class="field">Phone</div><div class="field">Service</div>
      <div class="field wide">Your Message</div>
    </div>
    <span class="btn">Send</span>
  </div>
</section>

<section class="offer">
  <h2>Want to Get 20% Off?</h2>
  <p>Save Time, Save Money, Save Yourself</p>
  <span class="btn">Contact Us Now</span>
</section>

<footer class="site-footer">
  <div class="brand"><i></i>Gwen Shines</div>
  <div class="vline"></div>
  <div class="contact-col">
    <h4>Contact Us Today!</h4>
    <div>Call @ <span class="phone">800.555.0142</span></div>
    <div>214 Maple Lane, Gainesville</div>
    <div>hello@gwenshines.net</div>
  </div>
  <div class="col" style="left:540px"><h4>Services</h4>Move-in/Out<br>Deep Cleaning<br>Bedrooms<br>Bathrooms<br>Kitchens</div>
  <div class="col" style="left:660px"><h4>Links</h4>Home<br>About Company<br>Why Gwen Shines<br>Reviews<br>Contact Us</div>
  <div class="col" style="left:800px"><h4>Opening Hours</h4>Monday – Friday<br>8am – 6pm<br>Saturday 9am – 2pm</div>
  <div class="social"><i></i><i></i><i></i><i></i></div>
  <div class="copy">© 2024 Gwen Shines. All rights reserved.</div>
</footer>

</body>
</html>
```